Web-site design for company trading in chemicals & lubricants

We need a standard 5 page web-site designed for our company based in Dubai, UAE.
The web-site should highlight our capacity to store material as well as distribute the same. The products we sell are basic chemicals - packed in bags as well as drums. Bags are big bags - 25 kgs each as well as drums - 200 litres each. We want to highlight the fact that we huge stocks of this material & can deliver by sea & road,
Please use this site as a ref - http://www.norvex-solvents.co.uk/
Besides this, we need a page dedicated to finished products that we are selling for use in the auto industry - lubricants, motor oils,brake-fluids, greases, coolants etc. This are packed in large drums as well as small cans.
It would be nice if the site could immediately also provide a ref. to our location - Dubai or that we are based in the Middle East.
We will provide our company logo for reference

```html
<!DOCTYPE html>
<html lang="en">
<head>
<meta charset="utf-8">
<title>Korvan – Chemicals &amp; Lubricants Trading</title>
<link href="https://fonts.googleapis.com/css2?family=Arimo:ital,wght@0,400;0,700;1,700&display=swap" rel="stylesheet">
<style>
:root{
  --brand-brown:#4a2a14;
  --logo-brown:#5a3418;
  --ink:#1e1e1e;
  --text:#6b6b6b;
  --muted:#8a8a8a;
  --accent:#e0701c;
  --panel:#232323;
  --panel-line:#555;
  --footer:#1b1b1b;
  --footer-bottom:#0e0e0e;
  --footer-text:#a8a8a8;
  --rule:#d6d6d6;
}
*{box-sizing:border-box;margin:0;padding:0}
html,body{width:1015px;height:1200px;overflow:hidden}
body{position:relative;background:#fff;font-family:"Arimo",Arial,sans-serif;color:var(--text)}
a{color:inherit}
.abs{position:absolute}

.top-band{left:0;top:0;width:1015px;height:5px;background:var(--brand-brown)}

.hero{left:61px;top:5px;width:893px;height:330px;box-shadow:0 12px 14px -8px rgba(0,0,0,.45)}
.hero-photo{width:100%;height:100%;background:linear-gradient(100deg,#7f95ab 0%,#2f6db0 30%,#1f5fa8 55%,#2a74bd 75%,#1a4f8c 100%)}
.hero-caption{left:224px;bottom:0;width:669px;height:47px;background:rgba(20,20,20,.78)}
.hero-caption p{position:absolute;left:27px;top:17px;color:#fff;font-weight:700;font-style:italic;font-size:13px;letter-spacing:.2px}
.hero-btn{position:absolute;left:493px;top:14px;width:62px;height:19px;background:#e9e2c8;color:#5a4a1a;font-size:8px;font-weight:700;font-style:italic;text-align:center;line-height:19px}
.hero-arrows{position:absolute;left:620px;top:16px}

.logo-box{left:61px;top:0;width:249px;height:90px;background:linear-gradient(#fafafa,#e6e6e6);box-shadow:0 2px 6px rgba(0,0,0,.35);z-index:2}
.logo-name{position:absolute;left:13px;top:46px;font-size:33px;font-weight:700;color:var(--logo-brown);letter-spacing:3px;line-height:1}
.logo-dot{position:absolute;left:196px;top:10px;width:40px;height:40px;border-radius:50%;background:var(--logo-brown)}

.main-nav{left:81px;top:90px;width:204px;height:218px;background:#fff;z-index:2}
.main-nav ul{list-style:none;padding:0 8px}
.main-nav li{height:42px;border-bottom:2px solid #ddd;display:flex;align-items:center;padding-left:22px;font-weight:700;font-style:italic;font-size:13px;color:#3b2a1c;letter-spacing:.3px}
.main-nav li:last-child{border-bottom:none}
.main-nav li span{margin-right:18px;font-style:normal;font-size:12px}

.finder{left:61px;top:364px;width:249px;height:129px;background:linear-gradient(#fdfdfd,#ececec);box-shadow:2px 3px 5px rgba(0,0,0,.25)}
.finder h2{position:absolute;left:18px;top:14px;font-size:15px;font-weight:400;color:#555}
.finder-input{position:absolute;left:17px;top:47px;width:206px;height:30px;border:1px solid #bbb;background:linear-gradient(#e4e4e4,#f8f8f8)}
.finder-btn{position:absolute;left:156px;top:87px;width:67px;height:22px;background:#1d1d1d;color:#fff;font-size:13px;text-align:center;line-height:22px}

.welcome{left:331px;top:368px;width:609px}
.welcome h1{font-size:16px;font-weight:400;color:var(--ink)}
.welcome h3{margin-top:13px;font-size:11.5px;font-weight:700;color:var(--ink)}
.welcome p{margin-top:7px;font-size:11px;line-height:17px;text-align:justify}
.more{color:var(--accent);font-size:11px;text-decoration:underline}

.product-list{left:66px;top:518px;width:200px}
.product-list h2{padding-left:37px;font-size:15px;font-weight:400;color:var(--accent);line-height:26px}
.flask{position:absolute;left:2px;top:0}
.product-list ul{list-style:none;margin-top:20px}
.product-list li{height:26.7px;padding-left:38px;position:relative;font-size:11px;color:#555;text-decoration:underline}
.product-list li svg{position:absolute;left:15px;top:2px}

.promo{left:64px;top:838px;width:184px;height:157px;background:linear-gradient(#0a86cc,#0a79bd)}

.sector{left:279px;width:390px}
.sector h2{padding-left:40px;font-size:15px;font-weight:400;color:var(--ink);line-height:26px}
.sector .icon{position:absolute;left:0;top:0}
.sector-photo{position:absolute;left:5px;top:45px;width:108px;height:95px}
.sector-body{position:absolute;left:131px;top:38px;width:257px}
.sector-body h3{font-size:11px;font-weight:700;color:var(--ink)}
.sector-body p{margin-top:10px;font-size:11px;line-height:17.5px;text-align:justify}
.sector .more{position:absolute;right:5px;top:134px}
.divider{left:279px;width:390px;height:1px;background:var(--rule)}

.sidebar{left:704px;top:512px;width:238px;height:481px;background:var(--panel);color:#ddd;overflow:hidden}
.sidebar h2{position:absolute;left:44px;font-size:15px;font-weight:400;color:#fff}
.side-rule{position:absolute;left:7px;width:221px;height:1px;background:var(--panel-line)}
.news{position:absolute;left:8px;width:218px}
.news p{padding-left:13px;position:relative;font-size:11px;line-height:17.5px;text-align:justify}
.news p::before{content:"";position:absolute;left:0;top:5px;border-left:5px solid #ddd;border-top:3.5px solid transparent;border-bottom:3.5px solid transparent}
.news .more{display:block;text-align:right;color:#ddd;margin-top:9px;margin-right:2px}
.contact dl{position:absolute;left:0;top:328px;width:238px;font-size:11px}
.contact dt{position:absolute;width:66px;text-align:right}
.contact dd{position:absolute;left:77px;line-height:17px}
.side-mark{position:absolute;left:12px;top:448px;font-size:30px;font-weight:700;letter-spacing:3px;color:#3a3a3a}
.side-mark-dot{position:absolute;left:176px;top:410px;width:48px;height:48px;border-radius:50%;background:#333}

.footer{left:0;top:1013px;width:1015px;height:142px;background:var(--footer);border-top:5px solid #2c2c2c}
.fcol{position:absolute;top:14px}
.fcol h4{font-size:12px;font-weight:400;color:#fff;margin-bottom:6px}
.fcol ul{list-style:none}
.fcol li{font-size:11px;color:var(--footer-text);line-height:19.6px;padding-left:12px;position:relative}
.fcol li::before{content:"";position:absolute;left:1px;top:8px;width:4px;height:4px;border-radius:50%;background:#888}
.fcol.find li{padding-left:12px}
.fcol.find li::before{display:none}
.map{position:absolute;left:803px;top:30px;width:142px;height:95px;background:linear-gradient(135deg,#d9d3c4,#b8cbd8 60%,#e3dcc9)}

.sub-footer{left:0;top:1155px;width:1015px;height:45px;background:var(--footer-bottom);color:#ccc;font-size:10.5px}
.sub-footer .copy{position:absolute;left:76px;top:17px}
.sub-footer .connect{position:absolute;left:733px;top:17px}
.social{position:absolute;left:816px;top:13px;display:flex;gap:7px}
.social span{width:20px;height:20px;border-radius:50%}
</style>
</head>
<body>

<div class="abs top-band"></div>

<section class="abs hero">
  <div class="hero-photo" role="img" aria-label="Warehouse racks stacked with blue and green chemical drums on wooden pallets"></div>
  <div class="abs hero-caption">
    <p>Cicero are also reproduced in their exact original accompanied.</p>
    <div class="hero-btn">View more</div>
    <svg class="hero-arrows" width="32" height="16" viewBox="0 0 32 16"><path d="M9 2 3 8l6 6" fill="none" stroke="#fff" stroke-width="3"/><path d="M23 2l6 6-6 6" fill="none" stroke="#fff" stroke-width="3"/></svg>
  </div>
</section>

<header class="abs logo-box">
  <div class="logo-dot"></div>
  <div class="logo-name">KORVAN</div>
</header>

<nav class="abs main-nav">
  <ul>
    <li><span>›</span>About Us</li>
    <li><span>›</span>Our Products</li>
    <li><span>›</span>Logistics</li>
    <li><span>›</span>Business Fields</li>
    <li><span>›</span>Contact Us</li>
  </ul>
</nav>

<section class="abs finder">
  <h2>Product Finder</h2>
  <div class="finder-input"></div>
  <div class="finder-btn">Search</div>
</section>

<section class="abs welcome">
  <h1>Welcome To Our Site</h1>
  <h3>Sed ut perspiciatis unde omnis iste natus error sit</h3>
  <p>Voluptatem accusantium doloremque laudantium, totam rem aperiam, eaque ipsa quae ab illo inventore veritatis et quasi architecto beatae vitae dicta sunt explicabo. Nemo enim ipsam voluptatem quia voluptas sit aspernatur aut odit aut fugit, sed quia consequuntur magni. Neque porro quisquam est, qui dolorem ipsum quia dolor sit amet, consectetur, adipisci velit, sed quia non numquam eius modi tempora incidunt</p>
</section>
<a class="abs more" style="left:883px;top:488px">View more</a>

<section class="abs product-list">
  <svg class="flask" width="24" height="28" viewBox="0 0 24 28"><path d="M9 2h6v8l7 14a2 2 0 0 1-2 3H4a2 2 0 0 1-2-3l7-14z" fill="#eee" stroke="#999"/><path d="M5 18h14l3 6a2 2 0 0 1-2 3H4a2 2 0 0 1-2-3z" fill="#e8801e"/></svg>
  <h2>Product List</h2>
  <ul>
    <li><svg width="12" height="10" viewBox="0 0 12 10"><path d="M0 3h6V0l6 5-6 5V7H0z" fill="#777"/></svg>Lorem ipsum dolo</li>
    <li><svg width="12" height="10" viewBox="0 0 12 10"><path d="M0 3h6V0l6 5-6 5V7H0z" fill="#777"/></svg>Consectetur adipiscing</li>
    <li><svg width="12" height="10" viewBox="0 0 12 10"><path d="M0 3h6V0l6 5-6 5V7H0z" fill="#777"/></svg>Donec imperdiet</li>
    <li><svg width="12" height="10" viewBox="0 0 12 10"><path d="M0 3h6V0l6 5-6 5V7H0z" fill="#777"/></svg>Interdum lorem</li>
    <li><svg width="12" height="10" viewBox="0 0 12 10"><path d="M0 3h6V0l6 5-6 5V7H0z" fill="#777"/></svg>Cursus ante loborti</li>
    <li><svg width="12" height="10" viewBox="0 0 12 10"><path d="M0 3h6V0l6 5-6 5V7H0z" fill="#777"/></svg>Vivamus eget libero</li>
    <li><svg width="12" height="10" viewBox="0 0 12 10"><path d="M0 3h6V0l6 5-6 5V7H0z" fill="#777"/></svg>Erat fringilla aliquam</li>
    <li><svg width="12" height="10" viewBox="0 0 12 10"><path d="M0 3h6V0l6 5-6 5V7H0z" fill="#777"/></svg>Integer tempor</li>
    <li><svg width="12" height="10" viewBox="0 0 12 10"><path d="M0 3h6V0l6 5-6 5V7H0z" fill="#777"/></svg>Elementum augue</li>
    <li><svg width="12" height="10" viewBox="0 0 12 10"><path d="M0 3h6V0l6 5-6 5V7H0z" fill="#777"/></svg>Sodales ipsum</li>
  </ul>
</section>

<div class="abs promo" role="img" aria-label="Promotional banner for a regional safety awareness event"></div>

<section class="abs sector" style="top:519px;height:150px">
  <svg class="icon" width="26" height="26" viewBox="0 0 26 26"><rect x="2" y="10" width="22" height="14" fill="#6f7d8a"/><rect x="5" y="3" width="4" height="9" fill="#b03a2e"/><rect x="12" y="6" width="4" height="6" fill="#8a96a2"/><rect x="6" y="15" width="4" height="4" fill="#dfe6ec"/><rect x="15" y="15" width="4" height="4" fill="#dfe6ec"/></svg>
  <h2>Industrial</h2>
  <div class="sector-photo" role="img" aria-label="Industrial chemical processing plant" style="background:linear-gradient(#b9c6cf,#7f7a70)"></div>
  <div class="sector-body">
    <h3>Sed ut perspiciatis unde omnis iste natus error sit</h3>
    <p>Nemo enim ipsam voluptatem quia voluptas sit aspernatur aut odit aut fugit, sed quia consequuntur magni. Neque porro quisquam est, qui dolorem ipsum quia dolor sit.</p>
  </div>
  <a class="more">View more</a>
</section>
<div class="abs divider" style="top:673px"></div>

<section class="abs sector" style="top:677px;height:150px">
  <svg class="icon" width="26" height="26" viewBox="0 0 26 26"><g transform="rotate(-40 13 13)"><rect x="2" y="8" width="22" height="10" rx="5" fill="#3a7fd0"/><path d="M13 8h6a5 5 0 0 1 0 10h-6z" fill="#f2b632"/></g></svg>
  <h2>Pharmaceutical</h2>
  <div class="sector-photo" role="img" aria-label="Hand holding a syringe" style="background:linear-gradient(135deg,#f4f4f4,#d9d2c8)"></div>
  <div class="sector-body">
    <h3>Sed ut perspiciatis unde omnis iste natus error sit</h3>
    <p>Nemo enim ipsam voluptatem quia voluptas sit aspernatur aut odit aut fugit, sed quia consequuntur magni. Neque porro quisquam est, qui dolorem ipsum quia dolor sit.</p>
  </div>
  <a class="more">View more</a>
</section>
<div class="abs divider" style="top:835px"></div>

<section class="abs sector" style="top:844px;height:150px">
  <svg class="icon" width="26" height="26" viewBox="0 0 26 26"><circle cx="13" cy="8" r="6" fill="#3a3a3a"/><path d="M2 25c0-7 5-10 11-10s11 3 11 10z" fill="#3a3a3a"/></svg>
  <h2>Personal Care</h2>
  <div class="sector-photo" role="img" aria-label="Dropper above a small amber cosmetic bottle" style="background:linear-gradient(#8fb247,#4f6e22 60%,#5a3a1c)"></div>
  <div class="sector-body">
    <h3>Sed ut perspiciatis unde omnis iste natus error sit</h3>
    <p>Nemo enim ipsam voluptatem quia voluptas sit aspernatur aut odit aut fugit, sed quia consequuntur magni. Neque porro quisquam est, qui dolorem ipsum quia dolor sit.</p>
  </div>
  <a class="more">View more</a>
</section>

<aside class="abs sidebar">
  <svg class="abs" style="left:11px;top:12px" width="24" height="16" viewBox="0 0 24 16"><rect x="1" y="1" width="22" height="14" fill="#ddd"/><rect x="4" y="4" width="7" height="6" fill="#888"/><path d="M13 5h7M13 8h7M4 12h16" stroke="#888" stroke-width="1.5"/></svg>
  <h2 style="top:11px">Latest News</h2>
  <div class="side-rule" style="top:39px"></div>
  <div class="news" style="top:51px"><p>Consectetur, adipisci velit, sed quia non numquam eius modi tempora incidunt.</p><a class="more">View more</a></div>
  <div class="news" style="top:126px"><p>Consectetur, adipisci velit, sed quia non numquam eius modi tempora incidunt.</p><a class="more">View more</a></div>
  <div class="news" style="top:201px"><p>Consectetur, adipisci velit, sed quia non numquam eius modi tempora incidunt.</p><a class="more">View more</a></div>

  <div class="contact">
    <svg class="abs" style="left:8px;top:284px" width="26" height="26" viewBox="0 0 26 26"><circle cx="13" cy="13" r="12" fill="#5aa13a"/><path d="M7 11c0-2 3-3 6-3s6 1 6 3l-2 1-1-2h-6l-1 2zM9 13h8l1 5H8z" fill="#fff"/></svg>
    <h2 style="top:288px">Contact Us</h2>
    <div class="side-rule" style="top:315px"></div>
    <dl>
      <dt style="top:0">E-mail :</dt><dd style="top:0">info @ korvan-trade.com</dd>
      <dt style="top:25px">Telepone :</dt><dd style="top:25px">410 552 7719<br>410 552 7720</dd>
      <dt style="top:70px">Fax :</dt><dd style="top:70px">410 552 7731<br>410 552 7732</dd>
    </dl>
  </div>
  <div class="side-mark-dot"></div>
  <div class="side-mark">KORVAN</div>
</aside>

<footer class="abs footer">
  <div class="fcol" style="left:68px"><h4>Home</h4><ul><li>About us</li><li>Our Products</li><li>Logistics</li><li>Business Fields</li><li>Contact Us</li></ul></div>
  <div class="fcol" style="left:201px"><h4>IIndustrial</h4><ul><li>Overview</li><li>Markets</li><li>Functionalities</li><li>Products</li><li>Partners</li></ul></div>
  <div class="fcol" style="left:332px"><h4>Pharmaceutical</h4><ul><li>Overview</li><li>API</li><li>Excipients</li><li>Custom Synthesis</li><li>Reagents &amp; Biochemicals</li></ul></div>
  <div class="fcol" style="left:517px"><h4>Personal Care</h4><ul><li>Overview</li><li>Markets</li><li>Functionalities</li><li>Products</li><li>Partners</li></ul></div>
  <div class="fcol find" style="left:664px"><h4>Find our Company</h4><ul><li>Nam a enim facilisis</li><li>magna scelerisque</li><li>V.I tincidunt augue</li><li>Dubai</li></ul></div>
  <div class="map" role="img" aria-label="Street map showing the company location in Dubai"></div>
</footer>

<div class="abs sub-footer">
  <span class="copy">Copyright © korvan-trade.com All rights reserved</span>
  <span class="connect">Connect with us :</span>
  <div class="social">
    <span style="background:#4a64a8"></span>
    <span style="background:#2fa9e0"></span>
    <span style="background:#f07a1a"></span>
    <span style="background:#555"></span>
    <span style="background:#6a2a8e"></span>
  </div>
</div>

</body>
</html>
```